Need modern simple design for magazine ad, apartment and condo roofer.

I need a half page magazine ad for a local roofer to publish in an industry magazine. Apartment associations industry. All types of roofs. Shingle and Flat
Need the design to be creative and modern, clean and simple. I do not want a busy design. One that stands out and makes a point quickly.
Logo must be prominent.
DO NOT USE PHOTOS FROM MY WEBSITE PLEASE. Looking for something new.
I work on entire complexes not houses.

Need to make sure our phone number and email address are listed at the bottom. Here is my website www.vorbelan.com
Want to stay away from standard clip arts of tools, homes, apartment buildings.
Half Horizontal 7.25 x 4.75
Ads should be in PDF and JPG format.

Target Market(s)

Apartment or Condo owners looking for large scale roofing projects

Industry/Entity Type

Roofing

Requirements
Must have
• Prominent Logo
Simple Clean Design
Create graphics
Not Busy
Should not have
• Clip Art
No Photos from my website

```html
<!DOCTYPE html>
<html lang="en">
<head>
<meta charset="utf-8">
<title>Vorbelan Multifamily Roofing – Half Page Ad</title>
<link rel="stylesheet" href="https://fonts.googleapis.com/css2?family=Arimo:wght@700&family=Sansita:wght@700&display=swap">
<style>
  :root {
    --stage: #545253;
    --brand-blue: #1f78c1;
    --brand-blue-soft: #9fc4e6;
    --steel: #8a8b8f;
    --steel-light: #c9cacd;
    --frame-band: #ebebec;
    --frame-line: #cfd0d2;
    --ink: #1d1b1c;
    --paper: #ffffff;
  }
  * { margin: 0; padding: 0; box-sizing: border-box; }
  html, body {
    width: 1200px; height: 1200px; overflow: hidden;
    background: var(--stage);
  }
  .ad {
    position: absolute; left: 63px; top: 307px;
    width: 1078px; height: 590px;
    border: 1px solid #111;
    overflow: hidden;
    background: var(--paper);
  }
  .ad__light {
    position: absolute; inset: 0;
    background:
      radial-gradient(ellipse at 62% 42%, rgba(255,255,255,1) 0%, rgba(255,255,255,0.85) 30%, rgba(222,230,238,0.7) 70%, rgba(235,240,245,0.8) 100%);
  }
  .ad__graphics { position: absolute; inset: 0; width: 1078px; height: 590px; }
  .brand-mark {
    position: absolute; left: 120px; top: 130px;
    width: 160px; height: 160px;
    background: var(--brand-blue);
  }
  .brand-name {
    position: absolute; left: 384px; top: 108px;
    font-family: "Arimo", Arial, sans-serif; font-weight: 700;
    color: var(--brand-blue);
    line-height: 1;
  }
  .brand-name__main { display: block; font-size: 104px; letter-spacing: 1px; }
  .brand-name__sub { display: block; font-size: 52px; margin-top: 22px; }
  .contact {
    position: absolute; left: 318px; top: 345px;
    list-style: none;
    font-family: "Sansita", "Trebuchet MS", sans-serif; font-weight: 700;
    color: var(--ink);
  }
  .contact__item { display: flex; align-items: center; position: relative; }
  .contact__item + .contact__item { margin-top: 10px; }
  .contact__icon { width: 46px; height: 46px; flex: none; margin-right: 20px; }
  .contact__text { font-size: 30px; letter-spacing: 0.5px; }
  .contact__item--address { align-items: flex-start; }
  .contact__item--address .contact__text { font-size: 24px; line-height: 1.4; margin-top: 2px; }
</style>
</head>
<body>
<main class="ad">
  <div class="ad__light" role="img" aria-label="Soft radiating light background in white, pale grey and pale blue"></div>

  <svg class="ad__graphics" viewBox="0 0 1078 590" aria-hidden="true">
    <defs>
      <linearGradient id="corner-blue" x1="0" y1="1" x2="1" y2="0">
        <stop offset="0" stop-color="#1f78c1"/>
        <stop offset="1" stop-color="#cfe2f3"/>
      </linearGradient>
    </defs>
    <!-- frame -->
    <rect class="frame-band" x="29" y="20" width="1020" height="549" fill="none" stroke="var(--frame-band)" stroke-width="20" opacity="0.9"/>
    <rect class="frame-line" x="48" y="46" width="982" height="492" fill="none" stroke="var(--frame-line)" stroke-width="4"/>
    <!-- faded outer stripes -->
    <polygon points="0,333 0,375 250,590 290,590" fill="var(--brand-blue-soft)" opacity="0.45"/>
    <polygon points="0,420 0,460 150,590 195,590" fill="var(--brand-blue-soft)" opacity="0.45"/>
    <polygon points="0,500 0,535 55,590 95,590" fill="var(--brand-blue-soft)" opacity="0.4"/>
    <!-- bottom-left blue stripes -->
    <polygon points="49,339 266,533 217,533 49,383" fill="var(--brand-blue)" opacity="0.85"/>
    <polygon points="49,407 192,533 151,533 49,445" fill="var(--brand-blue)" opacity="0.85"/>
    <polygon points="49,473 114,533 55,533 49,528" fill="var(--brand-blue)" opacity="0.85"/>
    <!-- bottom-right stripes -->
    <polygon points="1078,379 841,590 884,590 1078,420" fill="var(--steel)" opacity="0.9"/>
    <polygon points="1078,458 931,590 971,590 1078,500" fill="var(--steel)" opacity="0.9"/>
    <polygon points="976,590 1078,590 1078,505" fill="url(#corner-blue)"/>
  </svg>

  <div class="brand-mark" aria-hidden="true"></div>
  <h1 class="brand-name">
    <span class="brand-name__main">VORBELAN</span>
    <span class="brand-name__sub">Multifamily Roofing</span>
  </h1>

  <ul class="contact">
    <li class="contact__item">
      <svg class="contact__icon" viewBox="0 0 46 46" aria-hidden="true">
        <defs><radialGradient id="ball" cx="0.35" cy="0.3" r="0.8"><stop offset="0" stop-color="#d9dadc"/><stop offset="1" stop-color="#6f7073"/></radialGradient></defs>
        <circle cx="23" cy="23" r="22" fill="url(#ball)"/>
        <rect x="15" y="11" width="13" height="23" rx="2" fill="none" stroke="#fff" stroke-width="1.8"/>
        <circle cx="21.5" cy="30" r="1.3" fill="#fff"/>
        <path d="M31 19 q3 4 0 8 M34 17 q4 6 0 12" fill="none" stroke="#fff" stroke-width="1.4"/>
      </svg>
      <span class="contact__text">555.014.2290</span>
    </li>
    <li class="contact__item">
      <svg class="contact__icon" viewBox="0 0 46 46" aria-hidden="true">
        <circle cx="23" cy="23" r="22" fill="url(#ball)"/>
        <rect x="11" y="18" width="24" height="16" fill="none" stroke="#fff" stroke-width="1.8"/>
        <path d="M11 18 L23 27 L35 18 M11 34 L20 25 M35 34 L26 25" fill="none" stroke="#fff" stroke-width="1.6"/>
        <path d="M17 20 V11 H29 V20 M19 14 H27 M19 17 H27" fill="none" stroke="#fff" stroke-width="1.4"/>
      </svg>
      <span class="contact__text">info@vorbelan.com</span>
    </li>
    <li class="contact__item contact__item--address">
      <svg class="contact__icon" viewBox="0 0 46 46" aria-hidden="true">
        <circle cx="23" cy="23" r="22" fill="url(#ball)"/>
        <path d="M23 33 C17 25 15 22 15 18 a8 8 0 0 1 16 0 c0 4 -2 7 -8 15 z" fill="none" stroke="#fff" stroke-width="1.8"/>
        <circle cx="23" cy="18" r="3" fill="none" stroke="#fff" stroke-width="1.6"/>
        <line x1="16" y1="37" x2="30" y2="37" stroke="#fff" stroke-width="1.8"/>
      </svg>
      <span class="contact__text">214 Harlow Avenue, Suite 120,<br>Brenford, TX 75990</span>
    </li>
  </ul>
</main>
</body>
</html>
```